Historic Church website

We want our church website to feel warm, historic, and clean, modern, and easy to navigate. Dont use the anchor

Current website: https://www.meadowlarkfellowship.org/

Requirements
Should not have
• I would like to use the logo without the anchor

```html
<!DOCTYPE html>
<html lang="en">
<head>
<meta charset="utf-8">
<title>Meadowlark Fellowship</title>
<link href="https://fonts.googleapis.com/css2?family=Montserrat:wght@400;500;600;700;800;900&display=swap" rel="stylesheet">
<style>
:root{
  --gold:#d9a441;
  --gold-soft:#c8963a;
  --ink:#0c0a09;
  --espresso:#1a1210;
  --maroon:#3a1d13;
  --brown:#5a2e19;
  --cocoa:#2a1810;
  --cream:#f4eee6;
  --white:#ffffff;
  --muted:#cdbfb3;
}
*{box-sizing:border-box;margin:0;padding:0}
html,body{width:1200px;height:4408px;overflow:hidden}
body{font-family:'Montserrat',sans-serif;background:var(--ink);color:var(--white);position:relative}
section,header,footer{position:absolute;left:0;width:1200px}
.abs{position:absolute}
.btn{position:absolute;background:var(--gold);color:#2a1a0e;font-weight:700;font-size:13px;letter-spacing:.5px;text-transform:uppercase;border-radius:30px;display:flex;align-items:center;justify-content:center}
.dot{width:26px;height:26px;border-radius:50%;border:1.5px solid var(--white);display:inline-block;margin-left:8px}
.ph{position:absolute}
.h2{position:absolute;left:0;width:1200px;text-align:center;font-weight:800;font-size:32px;text-transform:uppercase;letter-spacing:.5px}

/* header + hero */
.hero{top:0;height:720px;background:radial-gradient(ellipse at 50% 40%,#6b4428 0%,#3b2416 45%,#1a0f09 100%)}
.topbar{top:18px;left:150px;font-size:12px;color:var(--white);display:flex;gap:22px;align-items:center}
.topbar span::before{content:"";display:inline-block;width:14px;height:14px;border-radius:50%;background:var(--gold);margin-right:7px;vertical-align:-3px}
.nav{top:66px;font-size:11px;font-weight:600;letter-spacing:1px;text-transform:uppercase;display:flex;gap:34px}
.nav-left{left:150px}.nav-right{left:745px}
.brand{top:14px;left:460px;width:280px;text-align:center;font-weight:700;font-size:30px;line-height:1;color:var(--white)}
.brand small{display:block;font-size:11px;letter-spacing:3px;margin-top:6px;font-weight:700}
.socials{top:14px;left:905px;display:flex}
.hero h1{top:268px;left:0;width:1200px;text-align:center;font-weight:900;font-size:62px;line-height:62px;letter-spacing:1px;text-transform:uppercase;text-shadow:0 3px 10px rgba(0,0,0,.6)}

/* about */
.about{top:720px;height:560px;background:var(--espresso)}
.about h2{top:48px;left:150px;width:470px;font-size:28px;line-height:32px;font-weight:800;text-transform:uppercase}
.about p{top:200px;left:150px;width:470px;font-size:11px;line-height:16px;color:var(--muted)}

/* anchor verse */
.verse{top:1280px;height:320px;background:linear-gradient(180deg,#3d1f14,#2b150e)}
.verse q{position:absolute;top:95px;left:500px;width:560px;font-weight:800;font-size:30px;line-height:38px;text-transform:uppercase;quotes:none}

/* events */
.events{top:1600px;height:900px;background:var(--ink)}
.card{position:absolute;top:220px;width:282px;height:500px;background:var(--white);color:#1a1210}
.card .photo{height:300px;position:relative}
.date{position:absolute;right:10px;bottom:14px;width:78px;height:82px;background:var(--cream);text-align:center;font-weight:800;font-size:26px;line-height:28px;padding-top:12px;color:#1a1210}
.date small{display:block;font-size:10px;font-weight:600;line-height:12px}
.card h3{font-size:20px;line-height:22px;font-weight:800;padding:22px 20px 8px}
.card p{font-size:11px;line-height:15px;padding:0 20px;color:#4a3a30}
.arrow{position:absolute;top:808px;width:38px;height:38px;border-radius:50%;border:2px solid var(--gold);display:flex;align-items:center;justify-content:center}

/* testimonials */
.testimonials{top:2500px;height:490px;background:radial-gradient(ellipse at center,#2a1812,#140c09)}
.quote{position:absolute;top:170px;width:430px;height:270px;background:#211410;padding:30px 34px;font-size:12px;line-height:18px;color:var(--muted)}
.quote::before{content:"";position:absolute;left:-12px;bottom:-12px;width:120px;height:120px;border-left:12px solid var(--gold);border-bottom:12px solid var(--gold);z-index:-1}
.quote cite{position:absolute;right:34px;bottom:26px;font-style:normal;font-weight:700;font-size:12px;color:var(--white);text-transform:uppercase}
.pager{position:absolute;top:462px;left:578px;display:flex;gap:6px}
.pager i{width:9px;height:9px;border-radius:50%;border:1.5px solid var(--white)}
.pager i:first-child{background:var(--white)}

/* visit */
.visit{top:2990px;height:490px;background:var(--ink)}
.visit .sub{top:148px;left:0;width:1200px;text-align:center;font-size:14px}
.box{position:absolute;top:210px;width:288px;height:205px;background:var(--brown);text-align:center;color:var(--gold)}
.box::after{content:"";position:absolute;inset:14px;border:1.5px solid var(--gold)}
.box h3{margin-top:68px;font-size:20px;line-height:24px;font-weight:800;text-transform:uppercase}
.box p{margin-top:12px;font-size:11px;color:var(--cream)}

/* newsletter */
.newsletter{top:3480px;height:532px;background:var(--cocoa)}
.field label{display:block;font-size:12px;margin-bottom:6px}
.field{position:absolute;left:620px;width:428px}
.field div{height:40px;border:1px solid #8d7566;background:transparent}

/* footer */
.site-footer{top:4012px;height:396px;background:#140d0a}
.contact{font-size:12px;line-height:30px}
.contact li{list-style:none}
.contact li::before{content:"";display:inline-block;width:12px;height:12px;border-radius:50%;background:var(--gold);margin-right:10px;vertical-align:-1px}
.links h4{font-size:18px;font-weight:800;text-transform:uppercase;margin-bottom:14px}
.links ul{list-style:none;font-size:12px;line-height:24px;columns:2;column-gap:50px}
.links li::before{content:"› ";color:var(--gold)}
.legal{top:330px;left:150px;font-size:11px;color:var(--muted);line-height:18px}
</style>
</head>
<body>

<header class="hero">
  <div class="ph" style="inset:0;background:linear-gradient(180deg,rgba(60,36,20,.55),rgba(30,18,10,.35) 50%,rgba(20,12,8,.9))" role="img" aria-label="Warm wood-paneled library with antique bookshelves, leather chairs and oil lamps"></div>
  <div class="abs topbar"><span>(555) 014-2278</span><span>info@meadowlarkfellowship.org</span></div>
  <nav class="abs nav nav-left"><span>About MF</span><span>Ministries</span></nav>
  <div class="abs brand">Meadowlark<br>Fellowship<small>EST. 1946</small></div>
  <nav class="abs nav nav-right"><span>Bible Studies</span><span>Sermon Library</span></nav>
  <div class="btn" style="top:12px;left:780px;width:110px;height:30px;font-size:11px">Donate</div>
  <div class="abs socials"><i class="dot"></i><i class="dot"></i><i class="dot"></i><i class="dot"></i></div>
  <h1 class="abs">Ancient Church.<br>Ancient Faith.<br>Eternal Truth.</h1>
  <div class="btn" style="top:540px;left:510px;width:180px;height:46px">Join Our Community</div>
</header>

<section class="about">
  <h2 class="abs">Meadowlark Fellowship is an independent Christian church in the Protestant tradition.</h2>
  <p class="abs">Our central tenets are found in our articles of faith and include belief in the deity and lordship of Jesus Christ, the Trinity, Jesus' perfect life, atoning death on the cross, bodily resurrection and ascension. Jesus' blood secures the inerrancy of the Bible in its original manuscripts, and our need for salvation through personal faith in Jesus Christ. In keeping with the prevailing perspective of the church during the centuries immediately following the Apostles, we teach premillennialism. That is the belief that Christ will physically and literally return to earth at the end of this age, to establish His kingdom on earth for a thousand years. At that time, He will establish a righteous rule in which the promises of Israel's covenants will be finally fulfilled, and afterward the kingdom will merge with the eternal kingdom.</p>
  <div class="btn" style="top:460px;left:150px;width:310px;height:44px;font-size:12px">If you can't join us in person click here for this week's sermon</div>
  <div class="ph" style="top:38px;left:650px;width:360px;height:370px;background:linear-gradient(135deg,#6e4526,#3a2416 60%,#1f130c)" role="img" aria-label="Antique map, candle, compass and old books on a wooden desk"></div>
</section>

<section class="verse">
  <div class="ph" style="top:30px;left:190px;width:220px;height:260px;background:radial-gradient(ellipse,#9c8a78,#4a2c1e 70%)" role="img" aria-label="Rope-wrapped ship anchor illustration"></div>
  <q>We have this hope as an anchor for the soul, firm and secure. - Heb 6:19</q>
</section>

<section class="events">
  <h2 class="h2" style="top:118px">Upcoming MF Events</h2>
  <article class="card" style="left:152px">
    <div class="photo" style="background:linear-gradient(160deg,#7a5332,#3a2314)" role="img" aria-label="Antique wall clock in a candlelit study"><div class="date">Jan<br>21<small>7:00 pm</small></div></div>
    <h3>Wednesday Night Bible Study</h3>
    <p>Come join our mid-week Bible Study from 7:00 - 8:30 pm. Meet us in the MF chapel. Contact church office for details.</p>
  </article>
  <article class="card" style="left:460px">
    <div class="photo" style="background:linear-gradient(160deg,#8a5e38,#41281a)" role="img" aria-label="Old maps and leather books spread across a desk"><div class="date">Jan<br>28<small>7:00 pm</small></div></div>
    <h3>Wednesday Night Bible Study</h3>
    <p>Come join our mid-week Bible Study from 7:00 - 8:30 pm. Meet us in the MF chapel. Contact church office for details.</p>
  </article>
  <article class="card" style="left:766px">
    <div class="photo" style="background:linear-gradient(160deg,#6a4a30,#2f1d12)" role="img" aria-label="Library room with globe and tall bookshelves"><div class="date">Feb<br>11<small>7:00 pm</small></div></div>
    <h3>Wednesday Night Bible Study</h3>
    <p>Come join our mid-week Bible Study from 7:00 - 8:30 pm. Meet us in the MF chapel. Contact church office for details.</p>
  </article>
  <div class="arrow" style="left:556px"><svg width="16" height="16" viewBox="0 0 16 16"><path d="M10 3 5 8l5 5" fill="none" stroke="#d9a441" stroke-width="2"/></svg></div>
  <div class="arrow" style="left:606px"><svg width="16" height="16" viewBox="0 0 16 16"><path d="M6 3l5 5-5 5" fill="none" stroke="#d9a441" stroke-width="2"/></svg></div>
</section>

<section class="testimonials">
  <h2 class="h2" style="top:78px">Testimonials</h2>
  <blockquote class="quote" style="left:150px">"The great need across evangelicalism is exposition of the Scriptures. I sense there is a departure from that, even amongst some of our own people who are entertaining the people, giving the people what they want, whereas we are called to teach the Word. It is the Word that is the power of God to salvation. It is the Word that is the power for Christian living, and the Word should be the center of that ministry. It may not be popular, it may not build mega-churches, but it will fulfill that to which they are called upon to do in ministry."<cite>Harold T. Whitcombe</cite></blockquote>
  <blockquote class="quote" style="left:620px">"In all our worship with us we extend a cordial welcome in the Name of Christ the Lord. Combining the warmth of a genuine Christian hospitality with the fervor of a personal, devotional application of the great doctrines and eternal truths of God's Word, this Church is committed to a Christ-honoring, Bible-teaching ministry in which every endeavor is made to maintain a sane balance in theology, avoiding the errors of fanatical cultism on the one hand, or a modernistic neo-orthodoxy on the other."<cite>Edwin R. Lowell, MF Founder</cite></blockquote>
  <div class="pager"><i></i><i></i><i></i></div>
</section>

<section class="visit">
  <h2 class="h2" style="top:96px">Visit Us This Sunday</h2>
  <div class="abs sub">Flip The Boxes For More Information</div>
  <div class="box" style="left:152px"><h3>Morning Worship<br>Service</h3><p>9:30 AM</p></div>
  <div class="box" style="left:456px"><h3>All Church<br>Lunch</h3><p>12:15 PM</p></div>
  <div class="box" style="left:760px"><h3>Afternoon<br>Adult Bible Study</h3><p>1:45 PM</p></div>
</section>

<section class="newsletter">
  <h2 class="h2" style="top:52px;line-height:38px">Sign Up For Our<br>Weekly Newsletter</h2>
  <div class="ph" style="top:160px;left:152px;width:440px;height:300px;background:linear-gradient(135deg,#d8c3a4,#8a6a48 60%,#4a3020)" role="img" aria-label="Open notebook and pen on a wooden table"></div>
  <div class="field" style="top:160px"><label>First Name *</label><div></div></div>
  <div class="field" style="top:240px"><label>Last Name *</label><div></div></div>
  <div class="field" style="top:320px"><label>Email *</label><div></div></div>
  <div class="btn" style="top:410px;left:620px;width:428px;height:40px;border-radius:0;font-size:12px">Click To Send</div>
</section>

<footer class="site-footer">
  <div class="abs brand" style="top:40px;left:150px;width:auto;text-align:left;font-size:28px">Meadowlark<br>Fellowship<small>EST. 1946</small></div>
  <ul class="abs contact" style="top:150px;left:150px">
    <li>2480 Linden Avenue<br><span style="padding-left:22px">Fairhaven, Oregon 97400</span></li>
    <li>(555) 014-2278</li>
    <li>info@meadowlarkfellowship.org</li>
  </ul>
  <div class="abs links" style="top:42px;left:490px">
    <h4>Quick Links</h4>
    <ul><li>Home</li><li>Who We Are</li><li>Visiting Us Sunday</li><li>Kids Church</li><li>Event Calendar</li><li>Our Ministries</li><li>Sunday Bible Studies</li><li>Sermons</li><li>Contact Us</li><li>Donate</li></ul>
  </div>
  <div class="ph" style="top:40px;left:790px;width:258px;height:210px;background:linear-gradient(135deg,#e8e4dc,#cfd6cf)" role="img" aria-label="Street map showing the church location"></div>
  <div class="abs" style="top:312px;left:150px;width:900px;height:1px;background:#3a2a22"></div>
  <p class="abs legal">© Copyright 2025 | Meadowlark Fellowship, Fairhaven, Oregon<br>All Rights Reserved | Site by Local Studio</p>
  <div class="abs socials" style="top:334px;left:900px"><i class="dot"></i><i class="dot"></i><i class="dot"></i><i class="dot"></i></div>
</footer>

</body>
</html>
```